Holiday Rental Leaflet

Want a DL size double sided leaflet to distribute via local businesses, markets, family and friends
HOLIDAY RENTALCarrickalinga - 17 Farrow Street Sleeps 8-10 (2 Queen, 1 Double, 2 bunks), 4 bedrooms, BIR to all bedrooms 2 Bathrooms, one with bath, 2 toilets Open Plan Lounge/Dining/Kitchen area Dining Table for 8 peopleReverse cycle airconditionerSlow combustion wood heaterTV/DVD, CD/RadioKitchen has m/wave, oven, fridge/freezer, dishwasherBBQ providedTimber decking with 2 outside tables and 12 chairs Washing Machine and dryer provided One street back from beach Smoke free zone No Pets
For further information or to book contact Joan on 0491 278 306 or email joanbirch62@veltranet.com.au

Requirements
Nice to have
• Have sent a variety of photos of the house. No need to use all of them, pick out the most relevant for the leaflet.

```html
<!DOCTYPE html>
<html lang="en">
<head>
<meta charset="utf-8">
<title>Holiday Rental Beach House Leaflet</title>
<link href="https://fonts.googleapis.com/css2?family=Crimson+Text:wght@400;700&family=Open+Sans:wght@400;600&family=PT+Sans+Narrow:wght@400;700&display=swap" rel="stylesheet">
<style>
:root{
  --teal:#50a791;
  --teal-dark:#3b8c77;
  --gold:#f3d38d;
  --gold-dot:#f0c97a;
  --ink:#5f6062;
  --rule:#d9d9d9;
  --page:#eceae6;
  --white:#ffffff;
}
*{margin:0;padding:0;box-sizing:border-box}
html,body{width:1200px;height:1093px;overflow:hidden;background:var(--page)}
body{position:relative;font-family:"PT Sans Narrow",Arial Narrow,sans-serif;color:var(--ink)}
.leaflet{position:absolute;width:394px;background:var(--white);box-shadow:0 4px 14px rgba(0,0,0,.18);overflow:hidden}
.leaflet--front{left:193px;top:68px;height:827px}
.leaflet--back{left:647px;top:152px;height:825px}
.photo{position:absolute;left:0;width:100%}
.badge{position:absolute;left:0;width:203px;height:56px;background:var(--teal);color:var(--white);font-family:"Open Sans",Arial,sans-serif;display:flex;align-items:center;padding-left:14px;gap:10px}
.badge svg{width:26px;height:24px;flex:none}
.badge__text{display:flex;flex-direction:column;line-height:1}
.badge__line{font-size:14px;padding:3px 0 2px;border-top:1px solid rgba(255,255,255,.8)}
.badge__main{font-size:18px;padding:2px 0 3px;border-bottom:1px solid rgba(255,255,255,.8)}
.wave{position:absolute;left:0;width:100%;display:block}
.title{position:absolute;left:0;width:100%;text-align:center;font-family:"Crimson Text",Georgia,serif}
.title__main{font-weight:700;font-size:26px;color:var(--teal-dark)}
.title__sub{font-size:21px;color:var(--ink);margin-top:-4px}
.divider{position:absolute;left:14px;right:12px;display:flex;align-items:center;gap:12px;font-family:"Crimson Text",Georgia,serif;font-size:14px;color:#9a9a9a;letter-spacing:.5px}
.divider::before,.divider::after{content:"";flex:1;height:1px;background:var(--rule)}
.thumbs{position:absolute;left:14px;top:453px;display:flex;gap:8px}
.thumb{width:117px;height:98px;border:1px solid #ccc}
.features{position:absolute;list-style:none;font-size:14px;line-height:1.15}
.features li{position:relative;padding-left:17px;margin-bottom:6px}
.features li::before{content:"›";position:absolute;left:0;top:2px;width:11px;height:11px;border-radius:50%;background:var(--gold-dot);color:var(--white);font-size:11px;line-height:9px;text-align:center;font-family:Arial,sans-serif;font-weight:700}
.features--back{font-size:13px}
.features--back li{margin-bottom:8px}
.tagline{position:absolute;left:0;width:100%;text-align:center;font-size:17px;text-transform:uppercase;color:var(--ink)}
.rule-band{position:absolute;left:0;width:100%;height:4px;background:var(--teal)}
.contact{position:absolute;left:0;width:100%;bottom:0;background:var(--teal);color:var(--white);text-align:center;padding-top:9px}
.contact__lead{font-size:13px}
.contact__phone{font-size:21px;font-weight:700;display:flex;justify-content:center;align-items:center;gap:6px;line-height:1.2}
.contact__phone svg{width:18px;height:18px}
.contact__email{font-size:12.5px}
</style>
</head>
<body>

<!-- Front side -->
<section class="leaflet leaflet--front">
  <div class="photo" style="top:0;height:330px;background:linear-gradient(180deg,#b9cfd8 0%,#7d8d80 35%,#6a7f62 60%,#9aae7a 100%)" role="img" aria-label="Photo of the elevated timber beach house with front deck, lawn and gum trees"></div>
  <svg class="wave" style="top:260px;height:80px" viewBox="0 0 394 80" preserveAspectRatio="none" aria-hidden="true">
    <path d="M0 30 C90 90 200 20 290 22 C340 23 370 30 394 40 L394 80 L0 80Z" fill="var(--gold)"/>
    <path d="M0 10 C70 70 180 60 260 42 C320 28 360 30 394 46 L394 80 L0 80Z" fill="var(--teal)"/>
    <path d="M0 38 C80 85 190 65 270 50 C330 40 365 42 394 55 L394 80 L0 80Z" fill="var(--white)"/>
  </svg>
  <div class="badge" style="top:35px">
    <svg viewBox="0 0 26 24" aria-hidden="true"><path d="M13 2 L25 12 H21 V22 H15.5 V15 H10.5 V22 H5 V12 H1Z" fill="#fff"/></svg>
    <div class="badge__text"><span class="badge__line">HOLIDAY RENTAL</span><span class="badge__main">BEACH HOUSE</span></div>
  </div>

  <div class="title" style="top:352px">
    <div class="title__main">Beautiful Family Home For RENT</div>
    <div class="title__sub">Carrickalinga - 17 Farrow Street</div>
  </div>

  <div class="divider" style="top:431px">INTERIOR VIEW</div>
  <div class="thumbs">
    <div class="thumb" style="background:linear-gradient(160deg,#b27a3c,#4a3a2e 60%,#2a2624)" role="img" aria-label="Lounge room with leather sofa"></div>
    <div class="thumb" style="background:linear-gradient(160deg,#e8e2d6,#d6953e 55%,#b06a22)" role="img" aria-label="Dining table with timber chairs"></div>
    <div class="thumb" style="background:linear-gradient(160deg,#c9955a,#d56b5b 50%,#35508f)" role="img" aria-label="Bedroom with striped bedspread"></div>
  </div>

  <ul class="features" style="left:18px;top:584px;width:180px">
    <li>Sleeps 8-10</li>
    <li>4 bedrooms<br>(2 Queen, 1 Double, 2 bunks)</li>
    <li>2 Bathrooms, one with bath</li>
    <li>2 toilets</li>
  </ul>
  <ul class="features" style="left:208px;top:584px;width:180px">
    <li>Open Plan Lounge/Dining<br>Kitchen area</li>
    <li>BIR to all bedrooms</li>
    <li>Dining Table for 8 people</li>
  </ul>

  <div class="tagline" style="top:700px">One street back from beach!</div>
  <div class="rule-band" style="top:737px"></div>
  <footer class="contact" style="height:81px">
    <div class="contact__lead">For further information or to book contact Joan on</div>
    <div class="contact__phone"><svg viewBox="0 0 18 18" aria-hidden="true"><circle cx="9" cy="9" r="8" fill="none" stroke="#fff" stroke-width="1.5"/><path d="M6 4.5 L7.8 4.5 L8.4 7 L7.2 7.8 C7.8 9.2 8.8 10.2 10.2 10.8 L11 9.6 L13.5 10.2 L13.5 12 C9 12.5 5.5 9 6 4.5Z" fill="#fff"/></svg>0491 278 306</div>
    <div class="contact__email">joanbirch62@veltranet.com.au</div>
  </footer>
</section>

<!-- Back side -->
<section class="leaflet leaflet--back">
  <div class="photo" style="top:95px;height:300px;background:linear-gradient(180deg,#3e82c9 0%,#6aa2d6 35%,#1d5b86 40%,#3b86a6 70%,#c9c1a6 100%)" role="img" aria-label="Photo of calm sea and sandy beach with headland in the distance"></div>
  <svg class="wave" style="top:80px;height:60px" viewBox="0 0 394 60" preserveAspectRatio="none" aria-hidden="true">
    <path d="M0 0 H394 V8 C330 8 250 40 150 34 C90 30 40 28 0 38Z" fill="var(--white)"/>
    <path d="M140 34 C230 40 320 0 394 8 V22 C340 12 260 40 140 34Z" fill="var(--gold)"/>
    <path d="M0 38 C50 26 100 30 150 34 C90 36 40 40 0 48Z" fill="var(--teal)"/>
  </svg>
  <svg class="wave" style="top:355px;height:60px" viewBox="0 0 394 60" preserveAspectRatio="none" aria-hidden="true">
    <path d="M0 0 C60 30 160 30 260 18 C320 10 360 8 394 14 V60 H0Z" fill="var(--gold)"/>
    <path d="M0 8 C60 40 160 42 260 28 C320 20 360 20 394 24 V60 H0Z" fill="var(--teal)"/>
    <path d="M0 20 C60 52 170 52 270 38 C330 30 365 30 394 34 V60 H0Z" fill="var(--white)"/>
  </svg>
  <div class="badge" style="top:31px">
    <svg viewBox="0 0 26 24" aria-hidden="true"><path d="M13 2 L25 12 H21 V22 H15.5 V15 H10.5 V22 H5 V12 H1Z" fill="#fff"/></svg>
    <div class="badge__text"><span class="badge__line">HOLIDAY RENTAL</span><span class="badge__main">BEACH HOUSE</span></div>
  </div>

  <ul class="features features--back" style="left:18px;top:428px;width:170px">
    <li>Reverse cycle airconditioner</li>
    <li>Slow combustion wood heater</li>
    <li>TV/DVD, CD/Radio</li>
    <li>Kitchen has m/wave, oven,<br>fridge/freezer, dishwasher</li>
  </ul>
  <ul class="features features--back" style="left:189px;top:428px;width:200px">
    <li>BBQ provided</li>
    <li>Washing Machine and dryer provided</li>
    <li>Timber decking with 2 outside tables<br>and 12 chairs</li>
    <li>Smoke free zone - No Pets</li>
  </ul>

  <div class="tagline" style="top:540px">One street back from beach!</div>
  <div class="photo" style="top:566px;height:158px;background:linear-gradient(170deg,#dfe9ee 0%,#5fb8b6 30%,#8a7458 55%,#5d5a55 100%)" role="img" aria-label="Photo of timber deck with outdoor tables and teal umbrellas"></div>
  <div class="rule-band" style="top:734px"></div>
  <footer class="contact" style="height:81px">
    <div class="contact__lead">For further information or to book contact Joan on</div>
    <div class="contact__phone"><svg viewBox="0 0 18 18" aria-hidden="true"><circle cx="9" cy="9" r="8" fill="none" stroke="#fff" stroke-width="1.5"/><path d="M6 4.5 L7.8 4.5 L8.4 7 L7.2 7.8 C7.8 9.2 8.8 10.2 10.2 10.8 L11 9.6 L13.5 10.2 L13.5 12 C9 12.5 5.5 9 6 4.5Z" fill="#fff"/></svg>0491 278 306</div>
    <div class="contact__email">joanbirch62@veltranet.com.au</div>
  </footer>
</section>

</body>
</html>
```